Pedicure Menu with 8 Scent Options

This design will be for a single page menu (front/back) that will display multiple different scent variations of a product. The purpose of this menu is to display to clients and show them the available options and benefits of each option.
The menu will be double sided.
The front page will include a header including brand logo and product name, and a total of 8 different scents including imagery and descriptive text.
The design should include the text provided for each scent. The design should have a layout that is structured/organized, easy to read, and has bright imagery that represents each scent.
An example is a modular layout using boxes that highlight a different scent within each box. Lavender scent should include aesthetic images of lavender flower and/or the color purple.
The back page will include brand logo, overall product description, and additional brief text that explains each step of the product.
The final size of the design should be 8.5"x11", produced in InDesign format, with all layers editable for future changes.
NOTE: Please carefully review the attached design brief that includes additional information, and all necessary text to include in the design.
Target Market(s)
Beauty/Spa Clients
Industry/Entity Type
Beauty
Requirements
Must have
- Bright and Vivid Imagery/Illustrations
Nice to have
- Background design that utilizes, lines, shapes, or other elements.

```html
<!DOCTYPE html>
<html lang="en">
<head>
<meta charset="utf-8">
<title>Lumera Deluxe Pedicure 4-Step Menu</title>
<link href="https://fonts.googleapis.com/css2?family=Montserrat:wght@500;700;800&family=Fira+Sans+Condensed:wght@400;500&display=swap" rel="stylesheet">
<style>
:root{
  --backdrop:#31331f;
  --paper:#ffffff;
  --card-bg:#f4f4ee;
  --band-bg:#f6f6f3;
  --ink:#111111;
  --ink-soft:#222222;
  --muted:#7a7a7a;
  --lavender:#9580b8;
  --mandarin:#f07021;
  --cucumber:#6cb33f;
  --jasmine:#b3d443;
  --rose:#d71f26;
  --mint:#1db991;
  --honey:#f4a025;
  --greentea:#2d6a2e;
  --bamboo:#8aa35a;
  --head:"Montserrat",sans-serif;
  --body:"Fira Sans Condensed",sans-serif;
}
*{box-sizing:border-box;margin:0;padding:0}
html,body{width:1200px;height:1200px;overflow:hidden}
body{background:var(--backdrop);position:relative;font-family:var(--body);color:var(--ink)}

.page{position:absolute;top:245px;width:552px;height:710px;background:var(--paper);overflow:hidden;box-shadow:0 2px 8px rgba(0,0,0,.35)}
.page--front{left:34px}
.page--back{left:617px}

.corner-decor{position:absolute;top:0;width:120px;height:120px;background:linear-gradient(135deg,rgba(138,163,90,.55),rgba(240,240,236,0) 70%)}
.corner-decor--left{left:0}
.corner-decor--right{right:0;background:linear-gradient(225deg,rgba(138,163,90,.55),rgba(240,240,236,0) 70%)}

.brand{position:absolute;top:28px;left:0;width:100%;display:flex;justify-content:center;align-items:center;gap:10px}
.brand__mark{width:10px;height:10px;border-radius:50%;background:var(--ink)}
.brand__name{font-family:var(--head);font-weight:500;font-size:40px;letter-spacing:1px;color:var(--ink);line-height:1}

.title{position:absolute;top:105px;left:0;width:100%;text-align:center;font-family:var(--head);font-weight:800;font-size:26px;color:var(--ink)}
.pill{position:absolute;top:145px;left:179px;width:198px;height:24px;border-radius:12px;background:var(--ink);color:#fff;font-family:var(--head);font-weight:700;font-size:17px;text-align:center;line-height:24px}

.scent-grid{position:absolute;left:16px;top:190px;width:522px;display:grid;grid-template-columns:254px 254px;grid-template-rows:repeat(4,114px);column-gap:14px;row-gap:14px}
.scent{background:var(--card-bg);border-radius:14px 14px 16px 16px;overflow:hidden;position:relative}
.scent__name{height:27px;line-height:27px;text-align:center;color:#fff;font-family:var(--head);font-weight:700;font-size:14px;border-radius:14px 14px 0 0}
.scent__image{position:absolute;left:8px;top:36px;width:62px;height:68px;border-radius:8px}
.scent__text{position:absolute;left:76px;top:33px;width:174px;font-size:8px;line-height:12.3px;text-align:justify;color:var(--ink-soft)}

.scent--lavender .scent__name{background:var(--lavender)}
.scent--lavender .scent__image{background:linear-gradient(160deg,#8e7cc3,#5d8a45)}
.scent--mandarin .scent__name{background:var(--mandarin)}
.scent--mandarin .scent__image{background:linear-gradient(160deg,#f7a23a,#ec6b12)}
.scent--cucumber .scent__name{background:var(--cucumber)}
.scent--cucumber .scent__image{background:linear-gradient(160deg,#f2a54a,#4f9a2e)}
.scent--jasmine .scent__name{background:var(--jasmine)}
.scent--jasmine .scent__image{background:linear-gradient(160deg,#f5f5ec,#7fb04a)}
.scent--rose .scent__name{background:var(--rose)}
.scent--rose .scent__image{background:linear-gradient(160deg,#d81f26,#8e0f14)}
.scent--mint .scent__name{background:var(--mint)}
.scent--mint .scent__image{background:linear-gradient(160deg,#5fae4a,#2f7a35)}
.scent--honey .scent__name{background:var(--honey)}
.scent--honey .scent__image{background:linear-gradient(160deg,#f1ede2,#e58b14)}
.scent--greentea .scent__name{background:var(--greentea)}
.scent--greentea .scent__image{background:linear-gradient(160deg,#4f9a3a,#3b3428)}

.intro{position:absolute;top:173px;left:33px;width:486px;text-align:justify;text-align-last:center;font-size:14.5px;line-height:20px;color:var(--ink)}

.step{position:absolute;left:0;width:552px}
.step--shaded{background:var(--band-bg)}
.step__photo{position:absolute;width:115px;height:90px;border:2px solid var(--ink);border-radius:18px 0 18px 0}
.step__title{position:absolute;font-family:var(--head);font-weight:700;font-size:17px;color:var(--ink)}
.step__desc{position:absolute;font-size:14.5px;color:var(--ink)}
.step__decor{position:absolute;border-radius:40%}
</style>
</head>
<body>

<section class="page page--front">
  <div class="corner-decor corner-decor--left" role="img" aria-label="Bamboo stalks and leaves illustration"></div>
  <div class="corner-decor corner-decor--right" role="img" aria-label="Bamboo stalks and leaves illustration"></div>
  <div class="brand"><span class="brand__mark"></span><span class="brand__name">Lumera Beauty &amp; Spa</span></div>
  <h1 class="title">Deluxe Pedicure 4-Step</h1>
  <div class="pill">Pick Your Pedicure</div>

  <div class="scent-grid">
    <article class="scent scent--lavender">
      <h2 class="scent__name">Lavender</h2>
      <div class="scent__image" role="img" aria-label="Bundle of lavender flowers"></div>
      <p class="scent__text">Melt away the stresses of the day with a delicate, sweet smell that is floral and woodsy at the same time. Lavender is a calming scent for relaxation that puts us in a better mood and helps create a sense of tranquility and peacefulness</p>
    </article>
    <article class="scent scent--mandarin">
      <h2 class="scent__name">Mandarin</h2>
      <div class="scent__image" role="img" aria-label="Whole and sliced mandarin oranges"></div>
      <p class="scent__text">Uplift your senses with a fruity and sweet aroma that promotes clarity, radiance and a smooth, even skin tone. A citrus blend of essential oils works great to polish dull skin, reduce wrinkles, and correct spots</p>
    </article>
    <article class="scent scent--cucumber">
      <h2 class="scent__name">Cucumber-Melon</h2>
      <div class="scent__image" role="img" aria-label="Cantaloupe slices and cucumbers"></div>
      <p class="scent__text">Jump into a refreshing blend of crisp cucumber, watery honeydew, and summer cantaloupe. Perfect for capturing the essence of a summer day. Bamboo and aloe extract help cool your skin after a day in the sun</p>
    </article>
    <article class="scent scent--jasmine">
      <h2 class="scent__name">Jasmine</h2>
      <div class="scent__image" role="img" aria-label="White jasmine flowers with leaves"></div>
      <p class="scent__text">Embrace the warmth of a rich and sensual floral scent that boosts your energy levels and helps make your day better and brighter. A symbol of purity, love, and beauty – Jasmine helps to reduce exhaustion, nervousness, and stress</p>
    </article>
    <article class="scent scent--rose">
      <h2 class="scent__name">Rose</h2>
      <div class="scent__image" role="img" aria-label="Cluster of red roses"></div>
      <p class="scent__text">Fall in love with a delicate floral twist of spicy and sweet that nourishes your skin and calms the mind. Essential oils help to reduce fine lines and protect the skin from UV damage</p>
    </article>
    <article class="scent scent--mint">
      <h2 class="scent__name">Mint</h2>
      <div class="scent__image" role="img" aria-label="Fresh mint sprigs"></div>
      <p class="scent__text">Rejuvenate your body with a cool mix of peppermint and spearmint that prevents skin damage, alleviates inflamed skin, and acts as a splash of tonic for the senses. Infused with eucalyptus to leave you clean, cool, and crisp</p>
    </article>
    <article class="scent scent--honey">
      <h2 class="scent__name">Milk &amp; Honey</h2>
      <div class="scent__image" role="img" aria-label="Jar of honey with dipper and glass of milk"></div>
      <p class="scent__text">Discover one of nature's most luxurious skin cleansers and softeners. Creamy milk is full of rich essential vitamins that supply abundant moisture and improves skin elasticity. Sweet honey contains antioxidants and other nutrients that slow down skin aging</p>
    </article>
    <article class="scent scent--greentea">
      <h2 class="scent__name">Green-Tea</h2>
      <div class="scent__image" role="img" aria-label="Fresh tea leaves over dried tea"></div>
      <p class="scent__text">Restore a sense of serenity with fragrant green tea extract that helps to relax the mind, reduces redness and swelling, and leaves the skin feeling hydrated, silky, and smooth. A natural detoxification that will supplies abundant moisture to the skin</p>
    </article>
  </div>
</section>

<section class="page page--back">
  <div class="corner-decor corner-decor--left" role="img" aria-label="Bamboo stalks and leaves illustration"></div>
  <div class="corner-decor corner-decor--right" role="img" aria-label="Bamboo stalks and leaves illustration"></div>
  <div class="brand"><span class="brand__mark"></span><span class="brand__name">Lumera Beauty &amp; Spa</span></div>
  <h1 class="title">Deluxe Pedicure 4-Step</h1>
  <p class="intro">Lumera Deluxe Pedicure 4-Step will transform your pedicure experience and immerse your senses into a floral paradise designed to rejuvenate your body. Sit back, relax, and enjoy.</p>

  <div class="step step--shaded" style="top:249px;height:113px">
    <div class="step__photo" style="left:93px;top:11px;background:linear-gradient(160deg,#e9dfd6,#b8a594)" role="img" aria-label="Spoon of bath salt over a foot soak basin"></div>
    <h2 class="step__title" style="left:232px;top:33px">1. Salt Soak</h2>
    <p class="step__desc" style="left:232px;top:60px">Detoxifies and deodorizes your feet.</p>
  </div>

  <div class="step" style="top:362px;height:113px">
    <div class="step__decor" style="left:8px;top:62px;width:66px;height:52px;background:linear-gradient(#9a9a9a,#5f5f5f)" role="img" aria-label="Stacked spa stones"></div>
    <h2 class="step__title" style="left:94px;top:38px">2. Sugar Scrub</h2>
    <p class="step__desc" style="left:94px;top:65px">Gently exfoliates dead skin.</p>
    <div class="step__photo" style="left:348px;top:11px;background:linear-gradient(160deg,#6f8f3a,#d9a98a)" role="img" aria-label="Feet with sugar scrub over a basin"></div>
  </div>

  <div class="step step--shaded" style="top:475px;height:114px">
    <div class="step__photo" style="left:93px;top:11px;background:linear-gradient(160deg,#eadfd6,#8a6a4e)" role="img" aria-label="Clay masque being applied to a leg"></div>
    <h2 class="step__title" style="left:232px;top:33px">3. Foot Masque</h2>
    <p class="step__desc" style="left:232px;top:60px">Cleanses pores for smoother skin.</p>
  </div>

  <div class="step" style="top:589px;height:121px">
    <div class="step__decor" style="left:0;top:20px;width:80px;height:101px;background:linear-gradient(#f3efe8,#cfc9bf)" role="img" aria-label="Lit spa candles"></div>
    <h2 class="step__title" style="left:94px;top:33px">4. Massage Lotion</h2>
    <p class="step__desc" style="left:94px;top:60px">Hydrates and soothes skin.</p>
    <div class="step__photo" style="left:348px;top:11px;background:linear-gradient(160deg,#f1e6df,#e2a994)" role="img" aria-label="Lotion being massaged onto a foot"></div>
    <div class="step__decor" style="left:478px;top:50px;width:74px;height:71px;background:linear-gradient(160deg,#8aa35a,#d8e0c6)" role="img" aria-label="Eucalyptus leaves sprig"></div>
  </div>
</section>

</body>
</html>
```